Vehicle Signage Design for a Renovation Company

We're a renovation company specialising in Home Renovations. The final design should communicate trust, credibility, and confidence. We need vehicle signage designed for our company utes (see attachment) / for our grey ute with the canopy/ and white use withou the canopyI've also attached our existing designs for the current vehicles (van and hatch back) to give you an idea of what we're after.In terms of content, there isn't much requirement for this due to the limited space on the ute - but happy to hear ideas on this.We've tried designing it ourselves - see attachment, but not happy with the result, would like more variations and ideas.Check out our website www.kestrelrenovations.co.nz for ideas on our branding/ style.
Updates

Target Market(s)

Home Owners

Industry/Entity Type

Residential Construction

Font styles to use
Sans Serif

Colors
3276b5
0355a3
33a6d7
3aa7d7
ffffff

Requirements
Must have
• Logo, Call to Action (website and number), Headline
Nice to have
• Strong sharp lines, a clean/sleek look
• It would be nice to have our offer on there (free design plans) / but we know space is limited

```html
<!DOCTYPE html>
<html lang="en">
<head>
<meta charset="utf-8">
<title>Kestrel Home Renovation – Ute Wrap Layout</title>
<link rel="stylesheet" href="https://fonts.googleapis.com/css2?family=Open+Sans:wght@600;700&family=Roboto+Condensed:wght@700;900&display=swap">
<style>
  :root {
    --navy: #0d2a6b;
    --navy-deep: #0a1c4c;
    --brand-blue: #0355a3;
    --mid-blue: #3276b5;
    --sky: #33a6d7;
    --red: #d7121f;
    --white: #ffffff;
    --charcoal: #3a3b3f;
    --steel: #8b8d92;
    --panel: #eef0f2;
    --bg-top: #f2f2f2;
    --bg-bottom: #d9d9d9;
  }
  html, body {
    margin: 0;
    width: 1200px;
    height: 1200px;
    overflow: hidden;
  }
  body {
    background: linear-gradient(180deg, var(--bg-top), var(--bg-bottom) 50%, var(--bg-top));
    font-family: "Roboto Condensed", "Arial Narrow", sans-serif;
  }
  .wrap-side {
    position: absolute;
    left: 50px;
    width: 1100px;
    height: 400px;
  }
  .wrap-side--driver { top: 150px; }
  .wrap-side--passenger { top: 700px; }
  .txt-cond { font-family: "Roboto Condensed", "Arial Narrow", sans-serif; font-weight: 700; }
  .txt-body { font-family: "Open Sans", Arial, sans-serif; font-weight: 600; }
  .brand-name { font-family: "Roboto Condensed", "Arial Narrow", sans-serif; font-weight: 900; fill: var(--white); }
  .brand-tag { fill: var(--navy-deep); }
  .services { fill: var(--white); }
  .phone { fill: var(--white); font-weight: 900; }
  .web { fill: var(--sky); }
  .offer-small { fill: var(--sky); }
  .ask-light { fill: var(--sky); }
  .ask-strong { fill: var(--white); }
  .ask-blue { fill: var(--sky); }
  .tag-text { fill: var(--white); }
  .social-ring { fill: none; stroke: var(--white); stroke-width: 1.5; }
  .pointer { fill: none; stroke: var(--white); stroke-width: 2; }
  .pointer-head { fill: var(--white); }
</style>
</head>
<body>

<!-- Driver side: vehicle front on the left -->
<svg class="wrap-side wrap-side--driver" viewBox="0 0 1100 400" aria-label="Driver side wrap layout">
  <defs>
    <linearGradient id="navyFade" x1="0" y1="0" x2="0" y2="1">
      <stop offset="0" stop-color="var(--brand-blue)"/>
      <stop offset="0.6" stop-color="var(--navy)"/>
      <stop offset="1" stop-color="var(--navy-deep)"/>
    </linearGradient>
  </defs>
  <rect class="body-base" x="0" y="110" width="1100" height="290" rx="30" fill="var(--charcoal)"/>
  <polygon class="body-navy" points="0,250 1100,118 1100,400 0,400" fill="url(#navyFade)"/>
  <polygon class="accent-stripe" points="0,244 1100,112 1100,120 0,254" fill="var(--white)"/>
  <polygon class="lower-band" points="0,390 1100,300 1100,400 0,400" fill="var(--steel)"/>
  <polygon class="lower-stripe" points="0,388 1100,298 1100,304 0,394" fill="var(--white)"/>

  <g class="offer-tag" transform="rotate(-6 120 215)">
    <rect x="60" y="198" width="170" height="26" fill="var(--red)"/>
    <text class="txt-cond tag-text" x="70" y="217" font-size="15">GET FREE 3D Design Plans</text>
  </g>

  <g transform="rotate(-6 320 300)">
    <rect x="240" y="225" width="170" height="170" fill="var(--panel)" role="img" aria-label="3D kitchen design rendering and floor plan sketches"/>
  </g>

  <g class="brand-block" transform="rotate(-6 620 300)">
    <text class="brand-name" x="450" y="270" font-size="96">Kestrel</text>
    <rect x="590" y="282" width="200" height="26" fill="var(--white)"/>
    <text class="txt-cond brand-tag" x="598" y="302" font-size="21">HOME RENOVATION</text>
    <text class="txt-cond services" x="480" y="326" font-size="17">BATHROOM • KITCHEN • FULL HOUSE RENOVATION</text>
  </g>

  <g class="contact-block" transform="rotate(-6 950 200)">
    <text class="txt-cond ask-light" x="780" y="172" font-size="14">THINKING ABOUT</text>
    <text class="txt-cond ask-strong" x="780" y="194" font-size="19">RENOVATING</text>
    <text class="txt-cond ask-blue" x="780" y="216" font-size="19">YOUR HOME?</text>
    <path class="pointer" d="M866 160 q18 -14 38 -6"/>
    <path class="pointer-head" d="M899 148 l10 8 -13 3 z"/>
    <rect x="905" y="165" width="195" height="40" fill="var(--red)"/>
    <text class="txt-cond phone" x="915" y="196" font-size="30">0800.246.135</text>
    <text class="txt-body web" x="915" y="224" font-size="11">www.kestrelrenovations.co.nz</text>
    <text class="txt-cond offer-small" x="945" y="238" font-size="9">FREE DESIGN TO BUILD CONSULTATION</text>
    <text class="txt-cond services" x="945" y="266" font-size="15">DESIGN • INSTALLATION</text>
    <g class="social-ring">
      <circle cx="990" cy="290" r="8"/><circle cx="1012" cy="290" r="8"/>
      <circle cx="1034" cy="290" r="8"/><circle cx="1056" cy="290" r="8"/>
    </g>
  </g>
</svg>

<!-- Passenger side: vehicle rear on the left -->
<svg class="wrap-side wrap-side--passenger" viewBox="0 0 1100 400" aria-label="Passenger side wrap layout">
  <defs>
    <linearGradient id="navyFadeB" x1="0" y1="0" x2="0" y2="1">
      <stop offset="0" stop-color="var(--brand-blue)"/>
      <stop offset="0.6" stop-color="var(--navy)"/>
      <stop offset="1" stop-color="var(--navy-deep)"/>
    </linearGradient>
  </defs>
  <rect class="body-base" x="0" y="110" width="1100" height="290" rx="30" fill="var(--charcoal)"/>
  <polygon class="body-navy" points="0,118 1100,250 1100,400 0,400" fill="url(#navyFadeB)"/>
  <polygon class="accent-stripe" points="0,112 1100,244 1100,254 0,120" fill="var(--white)"/>
  <polygon class="lower-band" points="0,300 1100,390 1100,400 0,400" fill="var(--steel)"/>
  <polygon class="lower-stripe" points="0,298 1100,388 1100,394 0,304" fill="var(--white)"/>

  <g class="contact-block" transform="rotate(6 150 200)">
    <rect x="10" y="135" width="200" height="40" fill="var(--red)"/>
    <text class="txt-cond phone" x="22" y="166" font-size="30">0800.246.135</text>
    <text class="txt-body web" x="22" y="194" font-size="11">www.kestrelrenovations.co.nz</text>
    <text class="txt-cond offer-small" x="22" y="208" font-size="9">FREE DESIGN TO BUILD CONSULTATION</text>
    <text class="txt-cond services" x="22" y="236" font-size="15">DESIGN • INSTALLATION</text>
    <g class="social-ring">
      <circle cx="40" cy="262" r="8"/><circle cx="62" cy="262" r="8"/>
      <circle cx="84" cy="262" r="8"/><circle cx="106" cy="262" r="8"/>
    </g>
    <path class="pointer" d="M320 158 q-18 -14 -45 -4"/>
    <path class="pointer-head" d="M278 147 l-10 8 13 3 z"/>
    <text class="txt-cond ask-light" x="240" y="176" font-size="14">THINKING ABOUT</text>
    <text class="txt-cond ask-strong" x="240" y="198" font-size="19">RENOVATING</text>
    <text class="txt-cond ask-blue" x="240" y="220" font-size="19">YOUR HOME?</text>
  </g>

  <g class="brand-block" transform="rotate(6 520 280)">
    <text class="brand-name" x="380" y="255" font-size="96">Kestrel</text>
    <rect x="520" y="270" width="200" height="26" fill="var(--white)"/>
    <text class="txt-cond brand-tag" x="528" y="290" font-size="21">HOME RENOVATION</text>
    <text class="txt-cond services" x="330" y="322" font-size="17">BATHROOM • KITCHEN • FULL HOUSE RENOVATION</text>
  </g>

  <g transform="rotate(6 820 300)">
    <rect x="750" y="230" width="170" height="170" fill="var(--panel)" role="img" aria-label="3D kitchen design rendering and floor plan sketches"/>
  </g>

  <g class="offer-tag" transform="rotate(6 1000 200)">
    <rect x="920" y="190" width="170" height="26" fill="var(--red)"/>
    <text class="txt-cond tag-text" x="930" y="209" font-size="15">GET FREE 3D Design Plans</text>
  </g>
</svg>

</body>
</html>
```